Bramble Creek Chiropractic

office phone- 913-555-0142
After Hour number 913-555-0187
Office address 27815 Hollister Rd. Maple Ridge Ks 66099
Dr. Marcus Fenwell, DC
I added 3 different types of logos proofs.
Specalizing in:
Family Wellness Care
Auto Accident
Workman Comp Injuries
Urgent Alternative Pain Relief
Non-operative Sports Injury Care

Marcus

```html
<!DOCTYPE html>
<html lang="en">
<head>
<meta charset="utf-8">
<title>Bramble Creek Chiropractic – Business Cards</title>
<link rel="stylesheet" href="https://fonts.googleapis.com/css2?family=Oswald:wght@400;500;600&display=swap">
<style>
  :root {
    --backdrop: #2f2b29;
    --card-white: #ffffff;
    --navy: #2b2a78;
    --signal-red: #e42a2a;
    --ink: #333333;
    --slate-light: #6d6b78;
    --slate-dark: #3c3b49;
    --on-dark: #ffffff;
    --muted-on-dark: #d8d8de;
  }
  * { margin: 0; padding: 0; box-sizing: border-box; }
  html, body {
    width: 1000px;
    height: 1200px;
    overflow: hidden;
    background: var(--backdrop);
    font-family: "Oswald", "Arial Narrow", sans-serif;
  }
  .canvas {
    position: relative;
    width: 1000px;
    height: 1200px;
  }
  .card {
    position: absolute;
    width: 723px;
    height: 423px;
  }

  /* Front */
  .card-front {
    left: 140px;
    top: 119px;
    background: var(--card-white);
  }
  .doctor-name {
    position: absolute;
    left: 35px;
    top: 128px;
    font-size: 27px;
    line-height: 30px;
    font-weight: 600;
    color: var(--navy);
  }
  .accent-bar {
    position: absolute;
    left: 0;
    top: 167px;
    width: 172px;
    height: 8px;
    background: var(--signal-red);
  }
  .contact-list {
    position: absolute;
    left: 35px;
    top: 196px;
    list-style: none;
    font-size: 17.5px;
    color: var(--ink);
    font-weight: 400;
  }
  .contact-list li { line-height: 28px; white-space: nowrap; }
  .contact-list li.gap { margin-top: 10px; }
  .contact-label { font-weight: 600; }
  .front-brand {
    position: absolute;
    right: 36px;
    top: 42px;
    display: flex;
    align-items: center;
    gap: 12px;
  }
  .brand-mark {
    width: 18px;
    height: 18px;
    border-radius: 50%;
    background: var(--signal-red);
  }
  .front-brand .brand-name {
    font-size: 22px;
    font-weight: 600;
    color: var(--navy);
    text-transform: uppercase;
    line-height: 1.1;
    text-align: right;
  }

  /* Back */
  .card-back {
    left: 125px;
    top: 638px;
    background: radial-gradient(ellipse at 50% 15%, var(--slate-light) 0%, #555462 45%, var(--slate-dark) 100%);
    color: var(--on-dark);
  }
  .back-brand {
    position: absolute;
    left: 0;
    right: 0;
    top: 88px;
    text-align center;
    text-align: center;
    font-size: 36px;
    line-height: 44px;
    font-weight: 600;
    text-transform: uppercase;
    color: var(--on-dark);
  }
  .specialties-heading {
    position: absolute;
    left: 0;
    right: 0;
    top: 158px;
    text-align: center;
    font-size: 21px;
    line-height: 32px;
    font-weight: 400;
  }
  .specialty {
    position: absolute;
    font-size: 18.5px;
    line-height: 26px;
    font-weight: 400;
    white-space: nowrap;
  }
  .specialty.left { right: 411px; text-align: right; }
  .specialty.right { left: 404px; }
  .specialty.center { left: 0; right: 0; text-align: center; }
  .website {
    position: absolute;
    left: 0;
    right: 0;
    top: 340px;
    text-align: center;
    font-size: 16px;
    line-height: 24px;
    letter-spacing: 2px;
    color: var(--muted-on-dark);
    font-weight: 400;
  }
</style>
</head>
<body>
<main class="canvas">

  <section class="card card-front" aria-label="Card front">
    <div class="front-brand">
      <span class="brand-mark" aria-hidden="true"></span>
      <span class="brand-name">Bramble Creek<br>Chiropractic</span>
    </div>
    <h1 class="doctor-name">Dr. Marcus Fenwell, DC</h1>
    <div class="accent-bar" aria-hidden="true"></div>
    <ul class="contact-list">
      <li><span class="contact-label">Office Phone:</span> 913-555-0142</li>
      <li><span class="contact-label">After Hour Number:</span> 913-555-0187</li>
      <li class="gap"><span class="contact-label">Email:</span> info@marcusfenwell.com</li>
      <li class="gap"><span class="contact-label">Office Address:</span>&nbsp; 27815 Hollister Rd. Maple Ridge Ks 66099</li>
    </ul>
  </section>

  <section class="card card-back" aria-label="Card back">
    <h2 class="back-brand">Bramble Creek Chiropractic</h2>
    <p class="specialties-heading">Specalizing in:</p>
    <p class="specialty left" style="top:223px">Family Wellness Care</p>
    <p class="specialty left" style="top:256px">Urgent Alternative Pain Relief</p>
    <p class="specialty right" style="top:226px">Workman Comp Injuries</p>
    <p class="specialty right" style="top:259px">Auto Accident</p>
    <p class="specialty center" style="top:295px">Non-operative Sports Injury Care</p>
    <p class="website">www.bramblecreekchiropractic.com</p>
  </section>

</main>
</body>
</html>
```